Bottled Beer Label Design

See Attached.
Updates
The beer label is printed on transparent pvc sticker, like the Valdermoor label. It meant that the unprinted part will be the color of the bottle. In this case it is amber color.
Attached please find photos of Valdermoor Bottle and label.
Thank you and best of luck.
Target Market(s)
Cater to the age grpoup in the 20's to early 40's in the Pubs and tothe la
Requirements
Must have
- See Attached.
Nice to have
- See Attached.
Should not have
- prefer not to have odd shaped label as the manufacturing will be easy and thus cheaper, and application of the label on to the bottle is less liable to develop defects

```html
<!DOCTYPE html>
<html lang="en">
<head>
<meta charset="utf-8">
<title>Keelstone Beer Label</title>
<link rel="stylesheet" href="https://fonts.googleapis.com/css2?family=Cormorant+Garamond:wght@600&family=Pinyon+Script&display=swap">
<style>
  :root {
    --page: #ffffff;
    --label-red: #cf1a20;
    --label-red-deep: #b5141a;
    --map-red: #c0161c;
    --map-line: #8e1014;
    --name-white: #ffffff;
    --tagline: #ffffff;
    --wheat-gold: #d9b877;
  }
  html, body {
    margin: 0;
    padding: 0;
    width: 1200px;
    height: 781px;
    overflow: hidden;
    background: var(--page);
  }
  .canvas {
    position: relative;
    width: 1200px;
    height: 781px;
    background: var(--page);
  }
  .label {
    position: absolute;
    left: 0;
    top: 0;
    width: 1200px;
    height: 781px;
  }
  .brand-name {
    font-family: "Cormorant Garamond", "Times New Roman", serif;
    font-weight: 600;
    fill: var(--name-white);
    font-size: 104px;
  }
  .tagline {
    font-family: "Pinyon Script", "Times New Roman", cursive;
    fill: var(--tagline);
    font-size: 27px;
  }
</style>
</head>
<body>
<main class="canvas">
  <svg class="label" viewBox="0 0 1200 781" xmlns="http://www.w3.org/2000/svg">
    <defs>
      <clipPath id="label-disc">
        <circle cx="392" cy="388" r="369"/>
      </clipPath>
      <linearGradient id="map-tone" x1="0" y1="0" x2="1" y2="1">
        <stop offset="0" stop-color="var(--map-red)"/>
        <stop offset="0.6" stop-color="var(--label-red)"/>
        <stop offset="1" stop-color="var(--map-line)"/>
      </linearGradient>
      <linearGradient id="wheat-tone" x1="0" y1="0" x2="0" y2="1">
        <stop offset="0" stop-color="var(--wheat-gold)" stop-opacity="0.55"/>
        <stop offset="1" stop-color="var(--wheat-gold)" stop-opacity="0.3"/>
      </linearGradient>
    </defs>

    <g class="label-disc" clip-path="url(#label-disc)">
      <rect class="label-body" x="20" y="15" width="745" height="745" fill="var(--label-red-deep)"/>
      <rect class="map-area" x="20" y="15" width="745" height="302" fill="url(#map-tone)"
            role="img" aria-label="Antique sea chart of Southeast Asia printed in dark red"/>
    </g>

    <g class="brand-block">
      <text class="brand-name" x="392" y="428" text-anchor="middle">Keelstone</text>
    </g>

    <g class="wheat-sprigs">
      <path class="wheat-left" d="M104 500 Q150 600 300 716 L262 722 Q130 630 96 520 Z"
            fill="url(#wheat-tone)" role="img" aria-label="Golden wheat sprig"/>
      <path class="wheat-right" d="M684 500 Q640 600 488 716 L526 722 Q656 630 692 520 Z"
            fill="url(#wheat-tone)" role="img" aria-label="Golden wheat sprig"/>
    </g>

    <g class="tagline-block" text-anchor="middle">
      <text class="tagline" x="392" y="520">Premium beer, handcrafted from the</text>
      <text class="tagline" x="392" y="567">finest ingredients. Proudly brewed and</text>
      <text class="tagline" x="392" y="614">bottled in Singapore.</text>
    </g>
  </svg>
</main>
</body>
</html>
```